Tri fold brochure for construction company

Looking for a tri fold brochure which utilizes black, teal and white colors. Logo must be on main page (several files with Logo attached)
Inside brochure.
1st Page - 3D photo/sketch/drawing of a complete residential high rise building with windows, balconies and elements of concrete and bricks.
2nd Page - Text which will outline company's main activities. file with text is attached.
3rd Page - photo/sketch/drawing of underground parking garage which shows columns/beams/walls/ and garage entrance/exit ramp. Can be multiple photos.
Back of brochure
1st page - company logo
2nd page - please propose something.
3rd page - company message with address and contact info (to be provided)
Back ground color of brochure should complement our logo/photos/sketches/drawings.
Alternative design options are welcome.

```html
<!DOCTYPE html>
<html lang="en">
<head>
<meta charset="utf-8">
<title>Northline Restoration Corp. – Tri-fold Brochure</title>
<link href="https://fonts.googleapis.com/css2?family=Roboto:wght@400;500;700&family=Roboto+Condensed:wght@400;700&display=swap" rel="stylesheet">
<style>
  :root{
    --teal:#17a98c;
    --teal-dark:#0b5f4f;
    --black:#0b0b0b;
    --ink:#222;
    --white:#ffffff;
    --stage:#d9d9d6;
  }
  *{box-sizing:border-box;margin:0;padding:0}
  html,body{width:1200px;height:1200px;overflow:hidden;background:var(--stage)}
  body{position:relative;font-family:"Roboto",sans-serif;color:var(--ink)}

  .sheet{position:absolute;left:282px;width:712px;height:502px;background:var(--white);overflow:hidden;box-shadow:0 4px 14px rgba(0,0,0,.25)}
  .sheet--outside{top:70px}
  .sheet--inside{top:640px}
  .panel{position:absolute;top:0;height:100%}

  /* outside: left panel */
  .panel--info{left:0;width:237px;padding:22px 18px 0 22px}
  .section-title{color:var(--teal);font-weight:500;font-size:10px;margin-bottom:6px}
  .star-list{list-style:none;font-size:8px;line-height:1.3}
  .star-list li{position:relative;padding-left:10px;margin-bottom:5px}
  .star-list li::before{content:"★";position:absolute;left:0;color:var(--teal)}
  .about{margin-top:19px}
  .about p{font-size:8px;line-height:1.27;text-align:justify;margin-bottom:8px}
  .photo{position:absolute}
  .photo--frame{left:22px;top:339px;width:192px;height:140px;background:linear-gradient(135deg,#c8c3b8,#8a8f92 55%,#c9a24a)}

  /* outside: middle panel */
  .panel--contact{left:237px;width:238px;text-align:center}
  .brand-mark{position:absolute;top:262px;left:0;width:100%}
  .brand-name{font-weight:700;font-size:12px;color:var(--ink);letter-spacing:.5px;line-height:1.1}
  .brand-sub{font-size:6px;font-weight:700;color:var(--teal);margin-top:2px;letter-spacing:.3px}
  .contact{position:absolute;left:0;width:100%;font-size:9.5px;font-weight:500;line-height:1.3}
  .contact svg{display:block;margin:0 auto 3px}
  .contact--web{top:323px}
  .contact--mail{top:362px}
  .contact--addr{top:393px}

  /* outside: cover */
  .panel--cover{left:475px;width:237px;background:var(--teal)}
  .cover-brand{height:89px;background:linear-gradient(180deg,#dff4f6,#eef9fa);display:flex;align-items:center;justify-content:center;gap:8px}
  .cover-brand .dot{width:14px;height:14px;background:var(--teal)}
  .cover-brand .brand-name{font-size:16px}
  .cover-brand .brand-sub{font-size:7.5px}
  .photo--hero{left:0;top:89px;width:237px;height:250px;background:linear-gradient(180deg,#c9d9e6 0%,#9fa8b0 60%,#6f7479 100%)}
  .cover-title{position:absolute;top:356px;left:0;width:100%;text-align:center;font-family:"Roboto Condensed",sans-serif;font-weight:700;line-height:1}
  .cover-title .line1{font-size:33px;color:var(--white)}
  .cover-title .line2{font-size:25px;color:#1d2b28;margin-top:2px}

  .skyline{position:absolute;left:0;bottom:0;width:100%}
  .skyline--dark{height:24px;background:var(--black)}
  .cover-url{position:absolute;right:58px;bottom:8px;color:var(--white);font-size:7.5px;letter-spacing:2px;z-index:2}

  /* inside */
  .photo--building{left:0;top:0;width:237px;height:100%;background:linear-gradient(160deg,#4fb3e0 0%,#8fcbe0 35%,#a9875b 70%,#4b3b2a 100%)}
  .panel--activities{left:237px;width:238px;background:var(--teal);color:var(--white);padding:21px 8px 0 21px;font-family:"Roboto Condensed",sans-serif}
  .act-title{font-size:12.5px;font-weight:700;line-height:1.2;margin-bottom:5px}
  .act-group{font-size:10px;font-weight:700;line-height:1.2;margin:0 0 1px}
  .act-group--second{margin-top:7px}
  .act-sub{font-size:8px;font-weight:400;line-height:12px;margin-top:8px}
  .act-group + .act-sub{margin-top:1px}
  .act-list{list-style:none;font-size:7.3px;line-height:9.3px}
  .act-list li{position:relative;padding-left:8px}
  .act-list li::before{content:"★";position:absolute;left:0;color:var(--teal-dark);font-size:5.5px}
  .photo--garage{left:475px;top:0;width:237px;height:100%;background:linear-gradient(180deg,#9c8056 0%,#7d8a8d 45%,#b89a6a 75%,#d0b48a 100%)}
  .skyline--light{height:20px;background:var(--white)}
</style>
</head>
<body>

<section class="sheet sheet--outside" aria-label="Brochure outside">
  <div class="panel panel--info">
    <h3 class="section-title">MISCELLANEOUS</h3>
    <ul class="star-list">
      <li>Railings remediation and replacement</li>
      <li>Outside garbage pad enclosures</li>
      <li>Retaining walls repair/replacement</li>
      <li>Weeping tile systems</li>
      <li>Safety bollards &amp; precast curbs installation</li>
      <li>Side walks, curbs, interlocking, asphalt and concrete pads</li>
      <li>Balconies and Parking garages painting</li>
      <li>Area drains replacements</li>
    </ul>
    <div class="about">
      <h3 class="section-title">ABOUT US</h3>
      <p>Lorem ipsum dolor sit amet, consectetur adipiscing elit, sed do eiusmod tempor incididunt ut labore et dolore magna aliqua. Quis ipsum suspendisse ultrices gravida. Risus commodo viverra maecenas accumsan lacus vel facilisis.</p>
      <p>Lorem ipsum dolor sit amet, consectetur adipiscing elit, sed do eiusmod tempor incididunt ut labore et dolore magna aliqua. Quis ipsum suspendisse ultrices gravida. Risus commodo viverra maecenas accumsan lacus vel facilisis.</p>
    </div>
    <div class="photo photo--frame" role="img" aria-label="Photo of a concrete building under construction with scaffolding"></div>
  </div>

  <div class="panel panel--contact">
    <div class="brand-mark">
      <div class="brand-name">NORTHLINE</div>
      <div class="brand-sub">RESTORATION CORP.</div>
    </div>
    <div class="contact contact--web">
      <svg width="16" height="16" viewBox="0 0 16 16"><circle cx="8" cy="8" r="7" fill="none" stroke="#17a98c" stroke-width="2"/><path d="M1 8h14M8 1c3 3 3 11 0 14M8 1c-3 3-3 11 0 14" stroke="#17a98c" stroke-width="1.2" fill="none"/></svg>
      www.yourwebsite.com
    </div>
    <div class="contact contact--mail">
      <svg width="16" height="12" viewBox="0 0 16 12"><rect x="0.5" y="0.5" width="15" height="11" fill="#17a98c"/><path d="M1 1l7 6 7-6" stroke="#fff" stroke-width="1.2" fill="none"/></svg>
      www.yourmailid@.com
    </div>
    <div class="contact contact--addr">
      <svg width="12" height="16" viewBox="0 0 12 16"><path d="M6 0a6 6 0 0 0-6 6c0 4.5 6 10 6 10s6-5.5 6-10a6 6 0 0 0-6-6z" fill="#17a98c"/><circle cx="6" cy="6" r="2.2" fill="#fff"/></svg>
      1234 your Addres<br>postal code, location
    </div>
  </div>

  <div class="panel panel--cover">
    <div class="cover-brand">
      <span class="dot"></span>
      <div>
        <div class="brand-name">NORTHLINE</div>
        <div class="brand-sub">RESTORATION CORP.</div>
      </div>
    </div>
    <div class="photo photo--hero" role="img" aria-label="Photo of an engineer in a hard hat in front of high-rise buildings under construction"></div>
    <h1 class="cover-title">
      <div class="line1">LOREM IPSUM</div>
      <div class="line2">DOLOR SIT AMET</div>
    </h1>
    <div class="cover-url">www.yourwebsite.com</div>
  </div>

  <div class="skyline skyline--dark" role="img" aria-label="Black city skyline silhouette along the bottom edge"></div>
</section>

<section class="sheet sheet--inside" aria-label="Brochure inside">
  <div class="panel photo photo--building" role="img" aria-label="Photo of a modern residential building with glass balconies at dusk"></div>

  <div class="panel panel--activities">
    <h2 class="act-title">OUR MAIN ACTIVITIES</h2>
    <h3 class="act-group">BUILDING ENVELOPE:</h3>
    <div class="act-sub">CONCRETE REPAIRS</div>
    <ul class="act-list"><li>Balcony slabs</li><li>Shear Walls</li><li>Beams &amp; Columns</li></ul>
    <div class="act-sub">SEALANT REPLACEMENT</div>
    <ul class="act-list"><li>Window wall and glazing system</li><li>Precast sealants</li><li>Masonry sealants</li><li>Balcony perimeter joints</li></ul>
    <div class="act-sub">MASONRY REPAIRS</div>
    <ul class="act-list"><li>Brick, Block &amp; Stone replacement</li><li>Tuck pointing</li><li>Through wall flashing</li><li>Coating</li></ul>
    <div class="act-sub">WATERPROOFING</div>
    <ul class="act-list"><li>Balconies &amp; Terraces thin system</li><li>Garbage &amp; Mechanical rooms</li></ul>
    <h3 class="act-group act-group--second">PARKING GARAGE STRUCTURES:</h3>
    <div class="act-sub">CONCRETE REPAIRS</div>
    <ul class="act-list"><li>Partial slab replacement</li><li>Top/under side repairs</li><li>Hydro demolition</li><li>Columns, Beams and Shear Walls</li><li>Catch basins &amp; trench drains</li><li>Staircases</li></ul>
    <div class="act-sub">WATERPROOFING</div>
    <ul class="act-list"><li>Vehicular thin system (drive aisles, parking bays, ramps, etc.)</li><li>Hot applied waterproofing (Ramps and Roof decks)</li><li>Expansion joints repairs/replacement</li><li>Mastic waterproofing system</li><li>Foundation wall crack injections</li><li>Crystalline waterproofing</li></ul>
    <div class="act-sub">RAMP REMEDIATION</div>
    <ul class="act-list"><li>Electric heating cables</li><li>Asphalt, Interlocking, Mastic and Concrete</li></ul>
  </div>

  <div class="panel photo photo--garage" role="img" aria-label="Photo of an underground parking garage with concrete columns and beams"></div>

  <div class="skyline skyline--light" role="img" aria-label="White city skyline silhouette along the bottom edge"></div>
</section>

</body>
</html>
```